Menu: A4 (double sided) Lunch/Dinner Menu (one side) + Pizza Menu (other side)

Hello.
We would like to create a new style of menus.
Must be easy to read - a summer feel, crisp, clean, beachy, possible retro feel, colours probably based on our website colours (see address below).
Simple and casual is best as we are a casual beachside Cafe.
This menu will be double sided therefore this job is 2 pages.
If you win this job we will have 2 or 3 more menus for you to create soon after (Drinks, Breakfast, possibly a small Kids menu).
The paper for these menus we expect will be a nice white paper which will then be matte laminated.
Colours possible are the green colour #3a6066, the terracotta on our website logo border and website buttons, maybe a little yellow but must be easy to read on white paper.
Black for text might be okay if this is your best design option.
Please view our website and take a feel for the business, location, the existing website branding and website colours we are trying to achieve, www.saltwrencafe.com.au
We prefer to avoid overwhelming the guest with too many colours on the menus (hence the white paper) as the building is so colourful (La Boca, Argentina, inspired) and the guest experience can be complimented via crisp easy to read menus.
IMPORTANT:
The menus provided please must be fully and easily editable by us in the future.
If you win the job, you must please provide clear instructions on how our staff can edit the menus in the future if project is delivered in Adobe format. Word is also an option for us if you like.
As such, we have attached some documents: the 2x Word documents for the text, 2x .pdf so you can see the fonts and style we were using previously (was printing on recycled brown paper then matte laminated).
If you wished to use the SeaLife Font (this is the existing Font for headings) please let us know as we purchased that font and can provide it.
We have also attached a menu from Quillmont Hotel which we feel has a nice retro feel.
Please include our Instagram in 1 place on the menu @saltwrencafe
Finally, please note,
we never wish to waste anyone's time so we will narrow down the submissions quickly based on first drafts (please know this is because we appreciate your effort and know your time is valuable) and we will then work with the top designer to finalise in a professional fashion.
Thank you.

```html
<!DOCTYPE html>
<html lang="en">
<head>
<meta charset="utf-8">
<title>Salt Wren Cafe – Lunch + Dinner and Pizza Menu</title>
<link href="https://fonts.googleapis.com/css2?family=Lilita+One&family=Poppins:wght@400;500;600;700;800&display=swap" rel="stylesheet">
<style>
  :root{
    --navy:#17407f;
    --terracotta:#b85a1b;
    --yellow:#efe61b;
    --ink:#1f1f1f;
    --veg:#4d9a3c;
    --gfo:#1b4a8f;
    --hot:#d42a2e;
    --paper:#ffffff;
    --backdrop:#d4d4d4;
  }
  *{box-sizing:border-box;margin:0;padding:0}
  html,body{width:1200px;height:960px;overflow:hidden}
  body{background:var(--backdrop);position:relative;font-family:"Poppins",sans-serif;color:var(--ink)}

  .page{position:absolute;top:74px;width:926px;height:1310px;background:var(--paper);transform:scale(.62);transform-origin:0 0;overflow:hidden}
  .page--lunch{left:14px}
  .page--pizza{left:612px}

  .title-box{position:absolute;left:167px;top:55px;width:594px;height:111px;background:var(--yellow);border:5px solid var(--terracotta);text-align:center;color:var(--navy)}
  .title-box h1{font-family:"Lilita One",sans-serif;font-weight:400;letter-spacing:2px}
  .page--lunch .title-box h1{font-size:60px;line-height:100px;transform:scaleX(1.12)}
  .page--pizza .title-box h1{font-size:64px;line-height:64px;margin-top:12px;letter-spacing:4px}
  .title-box .sub{font-weight:800;font-size:15px;margin-top:4px}

  .legend{position:absolute;top:181px;font-size:13px;display:flex;align-items:center;gap:7px;white-space:nowrap}

  .tag{display:inline-flex;align-items:center;justify-content:center;height:18px;min-width:38px;padding:0 6px;border-radius:9px;color:#fff;font-style:normal;font-weight:700;font-size:12px;vertical-align:middle;letter-spacing:.5px}
  .tag.veg{background:var(--veg)}
  .tag.gfo{background:var(--gfo)}
  .tag.hot{background:var(--hot)}
  .tag svg{width:18px;height:12px}
  .mild{font-size:13px;font-weight:400;margin:0 4px;text-transform:none}

  .heading{position:absolute;font-family:"Lilita One",sans-serif;font-weight:400;color:var(--navy);font-size:38px;line-height:40px;letter-spacing:.5px}

  .column{position:absolute;width:375px}
  .item{margin-bottom:12px}
  .column.entree .item{margin-bottom:15px}
  .name{display:flex;justify-content:space-between;align-items:flex-start;font-weight:500;font-size:19px;line-height:22px;color:#111}
  .name .label{max-width:330px}
  .column.mains .name,.pizza-col .name{text-transform:uppercase;font-size:18px;letter-spacing:.2px}
  .price{font-weight:500;font-size:19px}
  .desc{font-size:14px;line-height:21px;max-width:300px}
  .column.wide .desc{max-width:320px}
  .pizza-col .desc{max-width:340px}
  .add{display:flex;justify-content:space-between;font-size:14px;line-height:21px}
  .add .extra{font-size:14px}
  .note{font-size:12px;line-height:20px;padding-left:20px}
  .small{font-size:10px;font-weight:400;text-transform:none;margin-left:14px}
  .strong{font-weight:600}

  .rule{position:absolute;height:5px;background:var(--terracotta)}
  .social{position:absolute;display:flex;align-items:center;gap:8px;color:var(--navy);font-weight:600;font-size:20px}
  .social .mark{width:16px;height:16px;border:2px solid var(--navy);border-radius:3px}

  .platter-desc{position:absolute;left:480px;top:550px;width:320px;font-size:14px;line-height:21px}
  .platter-price{position:absolute;left:795px;width:60px;top:550px;text-align:right;font-size:19px;font-weight:500}
  .see-over{position:absolute;left:587px;top:1246px;color:var(--navy);font-weight:600;font-size:17px;letter-spacing:.3px}

  .allergy-bar{position:absolute;left:164px;top:219px;width:598px;height:30px;background:var(--terracotta);color:#fff;font-weight:700;font-size:14px;line-height:30px;text-align:center}
  .allergy-text{position:absolute;left:164px;top:256px;width:598px;font-size:8.5px;line-height:11px;text-align:center;padding:0 6px}
  .sides{position:absolute;top:316px;font-size:18px;font-weight:500;display:flex;gap:30px}
  .pizza-col{position:absolute;width:375px}
  .pizza-col .item{margin-bottom:13px}
  .pizza-col .item.gap{margin-top:8px}

  .art{position:absolute;left:470px;top:1005px;width:460px;height:310px;border-radius:55% 40% 0 30%;background:radial-gradient(circle at 45% 50%,#e84c5b 0%,#e6803a 40%,#f0b25a 62%,rgba(255,255,255,0) 75%)}
</style>
</head>
<body>

<section class="page page--lunch">
  <div class="title-box"><h1>LUNCH + DINNER</h1></div>
  <div class="legend" style="left:257px"><i class="tag veg">V</i> Vegetarian <span style="width:24px"></span> <i class="tag gfo">GFO</i> Gluten Friendly Optional, please ask</div>

  <h2 class="heading" style="left:71px;top:202px">ENTREE</h2>

  <div class="column entree" style="left:71px;top:252px">
    <div class="item"><div class="name"><span class="label">Garlic Bread (2) <i class="tag veg">V</i></span><span class="price">8</span></div></div>
    <div class="item"><div class="name"><span class="label">Salt &amp; Pepper Squid</span><span class="price">18</span></div><p class="desc">w/ thai dipping sauce</p></div>
    <div class="item"><div class="name"><span class="label">Duo of Dip <i class="tag veg">V</i></span><span class="price">14</span></div><p class="desc">w/ pita</p></div>
    <div class="item"><div class="name"><span class="label">Bowl of Chips <i class="tag veg">V</i></span><span class="price">11</span></div><p class="desc">w/ tomato sauce</p></div>
    <div class="item"><div class="name"><span class="label">Seasoned Wedges <i class="tag veg">V</i></span><span class="price">15</span></div><p class="desc">w/ sour cream &amp; sweet chilli</p></div>
  </div>

  <div class="column entree wide" style="left:480px;top:252px">
    <div class="item"><div class="name"><span class="label">Onion Rings (12) <i class="tag veg">V</i></span><span class="price">13</span></div><p class="desc">beer battered w/ tangy mayo</p></div>
    <div class="item"><div class="name"><span class="label">Vietnamese Spring Rolls (3)</span><span class="price">11</span></div><p class="desc">chicken, home-made</p></div>
    <div class="item"><div class="name"><span class="label">Bruschetta (1) <i class="tag veg">V</i></span><span class="price">10</span></div><p class="desc">w/ olive oil, tomato &amp; red onion salsa, balsamic glaze, feta</p></div>
  </div>

  <div class="social" style="left:42px;top:543px"><span class="mark"></span>saltwrencafe</div>
  <div class="rule" style="left:217px;top:554px;width:233px"></div>

  <h2 class="heading" style="left:480px;top:462px">SALT WREN PLATTER<br>for 2</h2>
  <p class="platter-desc">beer battered flathead, salt &amp; pepper squid, prawn skewers, grilled chicken, lamb &amp; chorizo, served with antipasto, dipping sauces, pita &amp; garlic bread (+45 pp)</p>
  <div class="platter-price">90</div>

  <h2 class="heading" style="left:71px;top:600px">MAINS</h2>

  <div class="column mains" style="left:71px;top:650px">
    <div class="item"><div class="name"><span class="label">The Fish &amp; Chips</span><span class="price">25</span></div><p class="desc">house-crumbed butterfish w/ chips, tartare &amp; side salad</p></div>
    <div class="item"><div class="name"><span class="label">Smokey Beef &amp; Bacon Cheese Burger</span><span class="price">25</span></div><p class="desc">w/ chips, onion rings, gerkins &amp; tangy mayo</p>
      <div class="add"><span>+ jalapenos</span><span class="extra">+2</span></div><div class="add"><span>+ pineapple</span><span class="extra">+2</span></div></div>
    <div class="item"><div class="name"><span class="label">Salt &amp; Pepper Squid</span><span class="price">31</span></div><p class="desc">golden tangles w/ chips, thai dipping sauce &amp; side salad</p></div>
    <div class="item"><div class="name"><span class="label">Seafood Basket <span class="small">(contains breadcrumbs)</span></span><span class="price">31</span></div><p class="desc">crumbed butterfish, grilled prawns, salt &amp; pepper squid, chips, tartare &amp; side salad</p></div>
    <div class="item"><div class="name"><span class="label">Atlantic Salmon</span><span class="price">31</span></div><p class="desc">served w/ mash, teriyaki sauce &amp; winter vegetables (contains breadcrumbs)</p></div>
    <div class="item"><div class="name"><span class="label">Chicken Parmigiana</span><span class="price">27</span></div><p class="desc">house-crumbed breast schnitzel, napoli sauce, mozzarella, chips &amp; side salad</p>
      <div class="add"><span>+ bacon and pineapple</span><span class="extra">+4</span></div><div class="add"><span>+ jalapenos and pineapple</span><span class="extra">+4</span></div></div>
  </div>

  <div class="column mains wide" style="left:480px;top:655px">
    <div class="item"><div class="name"><span class="label">New York Sirloin <i class="tag gfo">GFO</i></span><span class="price">38</span></div><p class="desc">400g MSA w/ mash &amp; winter vegetables</p><p class="desc strong">choose:</p>
      <div class="add"><span>mushroom gravy or classic gravy</span><span class="extra">+6</span></div>
      <div class="add"><span><b>or</b> surf ‘n’ turf <i class="tag gfo">GFO</i></span><span class="extra">+6</span></div>
      <p class="note">Please allow 35+ minutes for "well-done"</p></div>
    <div class="item"><div class="name"><span class="label">Chicken Caesar</span><span class="price">27</span></div><p class="desc">w/ bacon, anchovies, egg, caesar dress-ing, parmesan, spanish onion, garlic bread</p></div>
    <div class="item"><div class="name"><span class="label">Lamb Salad <i class="tag gfo">GFO</i></span><span class="price">30</span></div><p class="desc">skewers w/ traditional greek salad, tzatziki &amp; garlic bread</p><div class="add"><span>+ extra lamb</span><span class="extra">+8</span></div></div>
    <div class="item"><div class="name"><span class="label">Thai Chicken Curry <i class="tag hot"><svg viewBox="0 0 20 12"><path d="M5 9c4 0 7-2 8-6" stroke="#fff" stroke-width="2.4" fill="none" stroke-linecap="round"/><path d="M13 3l2-2" stroke="#fff" stroke-width="1.4"/></svg></i><span class="mild">mild</span><i class="tag gfo">GFO</i></span><span class="price">26</span></div><p class="desc">traditional recipe, w/ jasmine rice &amp; papadums</p></div>
    <div class="item"><div class="name"><span class="label">Beach Burger <i class="tag veg">V</i></span><span class="price">23</span></div><p class="desc">house-made pea &amp; corn ricotta fritter, pineapple, w/ wedges, onion rings, sweet chilli</p></div>
    <div class="item"><div class="name"><span class="label">Vegan Curry <i class="tag hot"><svg viewBox="0 0 20 12"><path d="M5 9c4 0 7-2 8-6" stroke="#fff" stroke-width="2.4" fill="none" stroke-linecap="round"/><path d="M13 3l2-2" stroke="#fff" stroke-width="1.4"/></svg></i><span class="mild">mild</span><i class="tag veg">V</i><i class="tag gfo">GFO</i></span><span class="price">24</span></div><p class="desc">chickpea &amp; pumpkin w/ fresh tomatoes &amp; basil, jasmine rice &amp; papadums</p></div>
  </div>

  <div class="rule" style="left:71px;top:1258px;width:498px"></div>
  <div class="see-over">FOR PIZZA PLEASE SEE OVER....</div>
</section>

<section class="page page--pizza">
  <div class="title-box"><h1>PIZZA</h1><p class="sub">ALL 12” with house-made tomato base &amp; mozzarella</p></div>
  <div class="legend" style="left:235px"><i class="tag veg">V</i> Vegetarian</div>
  <div class="legend" style="left:394px">Gluten Free base &nbsp; +$4</div>
  <div class="legend" style="left:570px">Vegan Cheese +$3</div>

  <div class="allergy-bar">Allergies? Please let us know!</div>
  <p class="allergy-text">All care is taken to cater for allergies including gluten, however our kitchen is small and we do not have separate preparation or cooking areas. As such, there is risk of cross-contact with your allergen and we are unable to guarantee allergen-free meals. Olives may very rarely contain pips.</p>

  <div class="sides" style="left:73px"><span>GARLIC BREAD</span><span>8</span></div>
  <div class="sides" style="left:378px"><span>GREEK SALAD</span><span>16</span></div>
  <div class="sides" style="left:681px;gap:14px"><span>GARDEN SALAD</span><span>12</span></div>
  <div class="rule" style="left:73px;top:357px;width:781px"></div>

  <h2 class="heading" style="left:73px;top:391px">STANDARD</h2>
  <h2 class="heading" style="left:483px;top:391px">GOURMET</h2>

  <div class="pizza-col" style="left:73px;top:447px">
    <div class="item"><div class="name"><span class="label">Hawaiian</span><span class="price">22</span></div><p class="desc">ham, pineapple</p></div>
    <div class="item"><div class="name"><span class="label">Margherita &nbsp;v</span><span class="price">22</span></div><p class="desc">marinated &amp; diced tomatoes, fresh basil</p></div>
    <div class="item"><div class="name"><span class="label">BBQ Chicken</span><span class="price">26</span></div><p class="desc">chicken, salami, tomato, spanish onion, bbq sauce</p></div>
    <div class="item"><div class="name"><span class="label">Chorizo <i class="tag hot"><svg viewBox="0 0 20 12"><path d="M5 9c4 0 7-2 8-6" stroke="#fff" stroke-width="2.4" fill="none" stroke-linecap="round"/><path d="M13 3l2-2" stroke="#fff" stroke-width="1.4"/></svg></i></span><span class="price">26</span></div><p class="desc">chorizo, salami, tomato, mushrooms, spanish onion</p></div>
    <div class="item"><div class="name"><span class="label">Salt Wren Special</span><span class="price">26</span></div><p class="desc">ham, salami, prawns, kalamata olives, roasted capsicum, mushrooms, spanish onion</p></div>
    <div class="item"><div class="name"><span class="label">Meat Lovers</span><span class="price">26</span></div><p class="desc">chicken, bacon, salami, ham, bbq sauce</p></div>
    <div class="item"><div class="name"><span class="label">Mona Lisa</span><span class="price">26</span></div><p class="desc">chicken, pineapple, ham, spanish onion, mushrooms</p></div>
    <div class="item"><div class="name"><span class="label">Puttanesca</span><span class="price">26</span></div><p class="desc">anchovies, capers, salami, kalamata olives, roasted capsicum, parmesan</p></div>
    <div class="item"><div class="name"><span class="label">Tropical Chicken <i class="tag hot"><svg viewBox="0 0 20 12"><path d="M5 9c4 0 7-2 8-6" stroke="#fff" stroke-width="2.4" fill="none" stroke-linecap="round"/><path d="M13 3l2-2" stroke="#fff" stroke-width="1.4"/></svg></i></span><span class="price">26</span></div><p class="desc">chicken, pineapple, spanish onion, chilli, tomato, mushrooms</p></div>
    <div class="item"><div class="name"><span class="label">Vegetarian &nbsp;v</span><span class="price">26</span></div><p class="desc">roasted capsicum, tomato, mushrooms, artichokes, kalamata olives, spanish onion</p></div>
    <div class="item gap"><div class="name"><span class="label">Build Your Own &nbsp;v</span><span class="price">26</span></div><p class="desc">tomato base, mozzarella &amp; four toppings</p></div>
  </div>

  <div class="pizza-col" style="left:483px;top:447px">
    <div class="item"><div class="name"><span class="label">Caveman</span><span class="price">29</span></div><p class="desc">chicken, lamb, pork sausage, chorizo, salami, bacon, spanish onion, caramelised onion, smokey bbq sauce</p></div>
    <div class="item"><div class="name"><span class="label">Spicy Prawn &amp; Basil Pesto <i class="tag hot"><svg viewBox="0 0 20 12"><path d="M5 9c4 0 7-2 8-6" stroke="#fff" stroke-width="2.4" fill="none" stroke-linecap="round"/><path d="M13 3l2-2" stroke="#fff" stroke-width="1.4"/></svg></i></span><span class="price">29</span></div><p class="desc">prawns, roasted capsicum, chilli, spring onion, basil pesto</p></div>
    <div class="item"><div class="name"><span class="label">Gourmet Vegetarian &nbsp;v</span><span class="price">29</span></div><p class="desc">pumpkin, eggplant, semi-dried tomatoes, roasted capsicum, red onion, bulgarian feta, kalamata olives, spinach</p></div>
    <div class="item"><div class="name"><span class="label">Johnny Ember <i class="tag hot"><svg viewBox="0 0 30 12"><path d="M3 9c4 0 7-2 8-6M15 9c4 0 7-2 8-6" stroke="#fff" stroke-width="2.4" fill="none" stroke-linecap="round"/></svg></i></span><span class="price">29</span></div><p class="desc">chilli jam, jalapeno peppers, mushrooms, bacon, chilli, chorizo, spanish onion</p></div>
    <div class="item"><div class="name"><span class="label">Lamb Pizza</span><span class="price">29</span></div><p class="desc">lamb, red onion, fresh tomato, tzatziki, spring onion</p></div>
    <div class="item"><div class="name"><span class="label">Los Pollos</span><span class="price">29</span></div><p class="desc">chicken, pumpkin, basil pesto, spinach, feta, pine nuts</p></div>
    <div class="item"><div class="name"><span class="label">Seafood Pizza</span><span class="price">29</span></div><p class="desc">array of seafood</p></div>
  </div>

  <div class="art" role="img" aria-label="Watercolour illustration of two pepperoni pizza slices"></div>

  <div class="social" style="left:46px;top:1245px"><span class="mark"></span>saltwrencafe</div>
  <div class="rule" style="left:219px;top:1256px;width:307px"></div>
</section>

</body>
</html>
```